website re-design - the brickfern studio

The Brickfern Studio is an existing website that we built using a new zealand based online CMS tool which is quite flexible and accomodates custom designs. You can check it here: http://www.pagequilt.co.nz/.

We have a logo already and the content on the website is OK.
The website can be found at www.thebrickfernstudio.com.au

mainly the homepage, but if the design is easily adapted to the other pages then, we will commission the winner to update these pages also.
Updates

Hi there,  I am uploading an image to be used as the main image on the homepage design,  so all submissions have the same image.

Target Market(s)

property developers, architects, builders, home buyers

Industry/Entity Type

Shop

Requirements
Must have
• Must utilise the existing CMS or at least be compatible to upload
Nice to have
• a promotional banner that can be turned off and on and changed as required as we offer different promotions over time.

```html
<!DOCTYPE html>
<html lang="en">
<head>
<meta charset="utf-8">
<title>The Brickfern Studio – Architectural Scale Models</title>
<link href="https://fonts.googleapis.com/css2?family=Ubuntu:wght@400;500;700&family=Arimo:wght@400;700&display=swap" rel="stylesheet">
<style>
:root{
  --bg:#f2ddb6;
  --paper:#ffffff;
  --orange:#f28a12;
  --orange-light:#ffb040;
  --green-dark:#0d2a06;
  --green-text:#4f7a0b;
  --olive:#a7a814;
  --ink:#222;
  --grey:#5a5a5a;
  --cream:#f5efe2;
  --red:#a00c0c;
  --rule:#d8d8d8;
}
*{margin:0;padding:0;box-sizing:border-box}
html,body{width:1152px;height:1200px;overflow:hidden;background:var(--bg)}
body{font-family:"Ubuntu",sans-serif;color:var(--ink)}
.stage{position:relative;width:1200px;height:1250px;transform:scale(.96);transform-origin:0 0}
.abs{position:absolute}
.page{left:90px;top:0;width:1018px;height:1182px;background:var(--paper);box-shadow:0 0 6px rgba(0,0,0,.15)}
.header-rule{left:90px;top:113px;width:1018px;height:8px;background:linear-gradient(#e2e2e2,#fff)}
.brand{left:158px;top:22px;display:flex;align-items:center;gap:16px}
.brand-mark{width:116px;height:68px;background:var(--orange)}
.brand-name{font-size:27px;color:#444;font-weight:400;letter-spacing:-.2px}
.brand-tag{left:294px;top:65px;font-size:13px;color:var(--orange);letter-spacing:.5px}
.contact{left:911px;top:20px;font-size:14px;line-height:18px;color:#444}
.contact .phone{color:var(--orange);font-weight:700;font-family:"Arimo",sans-serif;font-size:15px;margin-bottom:6px}
.nav{left:82px;top:147px;width:193px}
.nav a{display:block;height:34px;margin-bottom:4px;padding-left:40px;line-height:33px;font-size:16px;color:var(--orange);text-decoration:none;background:linear-gradient(#3a3a3a,#050505);box-shadow:1px 2px 3px rgba(0,0,0,.4)}
.nav a.active{background:linear-gradient(#ffc050,#f3910f);color:#3a2a10}
.offer{left:90px;top:418px;width:183px;height:347px;background:var(--cream)}
.offer h3{position:absolute;left:34px;top:10px;font-size:17px;color:var(--red);font-weight:500}
.offer .limit{position:absolute;left:34px;top:32px;font-size:12px;color:#222}
.offer-photo{position:absolute;left:0;top:54px;width:183px;height:138px;background:linear-gradient(160deg,#cfd2d6,#8e979c 60%,#5e6a62)}
.badge{position:absolute;left:119px;top:157px;width:64px;height:64px;border-radius:50%;background:var(--red);color:#fff;text-align:center;font-family:"Arimo",sans-serif;font-weight:700;font-size:19px;line-height:18px;padding-top:14px}
.badge small{font-size:15px}
.offer h4{position:absolute;left:16px;top:204px;font-size:14.5px;color:var(--orange);font-weight:500;line-height:18px}
.offer p{position:absolute;left:16px;top:248px;width:160px;font-size:12px;line-height:18px}
.offer .was{position:absolute;right:16px;top:306px;font-size:10px;text-decoration:line-through;font-weight:700;color:#555}
.offer .now{position:absolute;right:16px;top:318px;font-size:15px;color:var(--red);font-weight:700;font-family:"Arimo",sans-serif}
.kicker{left:313px;top:154px;font-family:"Arimo",sans-serif;font-weight:700;font-size:18px;color:var(--green-dark)}
.band{left:309px;top:183px;width:799px;height:42px;background:var(--green-dark)}
.band h1{position:absolute;left:21px;top:4px;font-family:"Arimo",sans-serif;font-size:26px;color:var(--orange);font-weight:700}
.hero-img{left:678px;top:150px;width:430px;height:236px;background:linear-gradient(150deg,#dcdce0,#8fb06a 45%,#3f6b2a 80%,#2b3a25);clip-path:polygon(4% 0,100% 0,100% 75%,2% 100%);box-shadow:0 4px 8px rgba(0,0,0,.3)}
.intro{left:314px;top:243px;width:345px;font-size:16.5px;line-height:24px;color:var(--grey)}
.easy{left:313px;top:392px}
.easy h2{position:absolute;left:37px;top:6px;white-space:nowrap;font-size:20px;color:var(--orange);font-weight:500}
.steps{left:312px;top:436px;width:474px;height:102px}
.step{position:absolute;left:38px}
.step .num{position:absolute;left:0;top:6px;width:37px;height:37px;border-radius:50%;background:var(--olive);color:#fff;text-align:center;line-height:37px;font-size:19px}
.step h3{position:absolute;left:49px;top:6px;white-space:nowrap;font-family:"Arimo",sans-serif;font-size:18px;color:var(--green-dark)}
.step p{position:absolute;left:49px;top:29px;white-space:nowrap;font-size:14px;color:#333}
.btn{display:block;width:271px;height:56px;border-radius:8px;background:linear-gradient(#ffb347,#f68c10);color:#3a2208;font-weight:700;font-size:19px;text-align:center;line-height:56px;text-decoration:none;box-shadow:0 1px 2px rgba(0,0,0,.2)}
.or{font-size:14px;color:#666;margin:6px 0 0 3px}
.or a{color:#6b4a20}
.rule{height:1px;background:var(--rule)}
.check h2{position:absolute;left:37px;top:-1px;white-space:nowrap;font-family:"Arimo",sans-serif;font-size:20px;color:var(--green-dark)}
.check .sub{position:absolute;left:37px;top:25px;white-space:nowrap;font-size:14px;color:var(--green-text)}
.list{left:317px;top:655px;width:460px;list-style:none}
.list li{position:relative;border-top:1px dotted #ccc;padding:4px 0 6px 33px;font-size:14px;line-height:18px;color:#333}
.list li::before{content:"";position:absolute;left:3px;top:9px;width:16px;height:16px;border:2px solid #c9c6a6}
.note{left:812px;top:607px;width:260px;height:165px;background:#f3f2e8;box-shadow:3px 4px 4px rgba(0,0,0,.15);padding:18px 16px;font-size:20px;line-height:30px;color:var(--green-text)}
.note b{color:var(--green-dark)}
.cta{left:309px;top:931px;width:787px;height:108px;background:var(--green-dark);border-radius:8px}
.cta p{position:absolute;left:32px;top:27px;width:440px;font-size:14px;line-height:18px;color:#fff}
.cta .act{position:absolute;left:494px;top:15px}
.cta .or,.cta .or a{color:#c7c62a}
.tailor{left:338px;top:1056px;width:730px;font-size:14px;line-height:18px;color:#666}
.social{left:310px;top:1146px;display:flex;gap:14px}
.social span{display:block;height:18px;padding:0 6px;border:1px solid #c9c9c9;border-radius:2px;font-size:11px;line-height:16px;color:#3b5a90;background:#f6f7fa}
.follow{left:990px;top:1142px;display:flex;align-items:center;gap:22px;font-size:12px;color:#666;font-style:italic}
.follow i{display:block;width:24px;height:24px;background:#3b5a98;border-radius:2px}
.footer-nav{left:92px;top:1192px;font-size:14px;color:#222}
.copy{left:912px;top:1192px;font-size:14px;color:#444}
</style>
</head>
<body>
<div class="stage">
  <div class="abs page"></div>
  <div class="abs header-rule"></div>

  <div class="abs brand"><span class="brand-mark"></span><span class="brand-name">THE BRICKFERN STUDIO</span></div>
  <div class="abs brand-tag">ARCHITECTURAL SCALE MODELS</div>
  <div class="abs contact">
    <div class="phone">Phone: (08) 6140 0377</div>
    118 Wattle Parade<br>Northbridge, WA 6003<br>Australia
  </div>

  <nav class="abs nav">
    <a href="#">Home</a>
    <a href="#" class="active">Gallery</a>
    <a href="#">Order Online</a>
    <a href="#">Get a Quote</a>
    <a href="#">3D Visualization</a>
    <a href="#">Contact</a>
    <a href="#">About Us</a>
  </nav>

  <aside class="abs offer">
    <h3>Special Offer</h3>
    <div class="limit">for a limited time!</div>
    <div class="offer-photo" role="img" aria-label="Scale model of a two-storey house with a car and pool"></div>
    <div class="badge">50%<br><small>Off</small></div>
    <h4>Integer Porta<br>Dignissim Augue</h4>
    <p>Facilisis ridiculus adipiscing porttitor, sit arcu parturient a! Habitasse!</p>
    <div class="was">$ 000.00</div>
    <div class="now">$ 000.00</div>
  </aside>

  <div class="abs kicker">A picture’s worth a thousand words...</div>
  <div class="abs band"><h1>A model says it all...</h1></div>
  <div class="abs hero-img" role="img" aria-label="Architectural scale model of a residential estate with townhouses and green landscaping"></div>
  <p class="abs intro">Getting an architectural model produced can be expensive and time consuming, but it can also add a lot of value to a project.&nbsp; A scale model lets everyone involved, get a very clear understanding of your building.</p>

  <div class="abs easy">
    <svg width="24" height="34" viewBox="0 0 24 34"><circle cx="11" cy="11" r="10" fill="#ffd94a"/><rect x="6" y="20" width="10" height="8" rx="2" fill="#bbb"/></svg>
    <h2>It’s This Easy!</h2>
    <svg class="abs" style="left:192px;top:12px" width="36" height="28" viewBox="0 0 36 28" fill="none" stroke="#777" stroke-width="1.5"><path d="M2 6c10-6 22-4 22 4 0 6-9 6-8 0 1-5 10-4 12 6"/><path d="M24 14l4 4 3-6"/></svg>
  </div>

  <div class="abs steps">
    <svg class="abs" style="left:0;top:0" width="26" height="102" viewBox="0 0 26 102" fill="none" stroke="#ddd" stroke-width="6"><path d="M24 4c-10 0-12 4-12 14v20c0 8-4 12-10 13 6 1 10 5 10 13v20c0 10 2 14 12 14"/></svg>
    <svg class="abs" style="left:448px;top:0" width="26" height="102" viewBox="0 0 26 102" fill="none" stroke="#ddd" stroke-width="6"><path d="M2 4c10 0 12 4 12 14v20c0 8 4 12 10 13-6 1-10 5-10 13v20c0 10-2 14-12 14"/></svg>
    <div class="step" style="top:0"><span class="num">1</span><h3>Order</h3><p>Order online or fill the quote form</p></div>
    <div class="step" style="top:53px"><span class="num">2</span><h3>Get Your Model</h3><p>We’ll build your model and deliver it right to your door</p></div>
  </div>

  <div class="abs" style="left:802px;top:457px">
    <a class="btn" href="#">Order Your Model Now »</a>
    <div class="or">or, <a href="#">Get a Quote</a></div>
  </div>

  <div class="abs rule" style="left:309px;top:567px;width:799px"></div>

  <div class="abs check" style="left:313px;top:596px">
    <svg width="28" height="28" viewBox="0 0 28 28"><circle cx="14" cy="14" r="13" fill="#3aa6e0"/><text x="14" y="20" font-size="17" font-family="Arimo,sans-serif" font-weight="700" fill="#fff" text-anchor="middle">?</text></svg>
    <h2>Do I need a model right now?</h2>
    <div class="sub">Here’s a quick checklist for you</div>
  </div>

  <ul class="abs list">
    <li>Are you undertaking a new apartment development or land development and need a model for council approval or marketing purposes?</li>
    <li>Are you getting a new house designed and built and need a clear understanding of how it will look?</li>
    <li>Are you an architect or building designer looking for a more affordable way to add to your service?</li>
    <li>Are you wanting to clarify in your own mind how your new building sits on its site?</li>
    <li>Are you looking to for a way to market your buildings in an effective and affordable format that everyone can relate to?</li>
  </ul>

  <div class="abs note">If you answered <b>YES</b> to any of these questions, then you <b style="font-weight:500">Should Be</b> using the brickfern studio.</div>
  <svg class="abs" style="left:800px;top:595px" width="28" height="28" viewBox="0 0 28 28"><circle cx="14" cy="14" r="13" fill="#3aa6e0"/><text x="14" y="20" font-size="16" font-family="Arimo,sans-serif" font-style="italic" font-weight="700" fill="#fff" text-anchor="middle">i</text></svg>

  <section class="abs cta">
    <p>We have made the system very easy to use, so all you need to do is click your way to your new scale model.&nbsp; Just follow the prompts and away you go.</p>
    <div class="act">
      <a class="btn" href="#">Order Your Model Now »</a>
      <div class="or">or, <a href="#">Get a Quote</a></div>
    </div>
  </section>

  <p class="abs tailor">You can tailor your model to suit your project and budget needs.&nbsp; There are various add-ons such as a display case, internal walls, acrylic windows, people trees and cars and site contours as well as a scaled pricing structure based on the size of your building.</p>

  <div class="abs rule" style="left:309px;top:1130px;width:799px"></div>
  <div class="abs social"><span>Share</span><span>Like</span><span>Post</span></div>
  <div class="abs follow">Follow us <i></i></div>

  <div class="abs footer-nav">Home | Gallery | Order | Quote | 3D | Contact | About</div>
  <div class="abs copy">© Copyright The Brickfern Studio</div>
</div>
</body>
</html>
```